orOS app - Personal finance : Loan Calculator

Hi,
I need an app design for an orOS application that respects the last Brindle guidelines :
https://developer.brindlework.com/ios/human-interface-guidelines/graphics/app-icon/

I speak english and french.

Design should include logo, splashscreen and 4 main features as detailed further.

This application is a loan calculator that computes monthly payments, amortization tables, credit capacity.

App desc, screens and old logo here : https://apps.brindlework.com/us/app/debt-path-housing-calculator/id508213774?mt=8

1. SPIRIT
The ideas to express in the design : simplicity, reliability, efficiency.
Use of graphics instead of words/number is always better.

2. ICON
No text, no letter in the logo.
Existing logo is not modern, too detailed.

3. SPLASHSCREEN

4. COLOR / Design style
OROS 10 style
Modern colours
If you need one color as base use the blue

5. FEATURES/APP PAGES
Attached are the current screens to adapt with the new design :

Must Have:
- Loan Calculator (1screen uploaded in 2 parts)
- Loan Amortization : yearly table, monthly table and export (2 screens roughly the same +1)
- Saved Loans (1 screen), feature improvement could be to display what is left to pay for all loans, see saved loans idea 1 and 2 (I prefer the design of idea 1).
- Credit Capacity (1 screen uploaded in 2 parts), see also the inspiration file to propose a more visual interface (with chart/graphics)

Nice to have :
- refinance calculator (1 screen uploaded in 2 parts)
- Market rates table (1 screen)

Target Market(s)

1. Professionals in finance, real estate, car where a loan can be proposed to their customers -
2. Individuals that want to apply for a loan

Industry/Entity Type

Loan

Font styles to use
Serif
Sans Serif

Requirements
Must have
• Icon (see App Icon Guidelines in uploaded files)
• Splashscreen
• 4 Top features : Loan Calculator, Loan amortization with export, Credit capacity, Saved loans.
Nice to have
• Other screens : Refinance calculator, Market rates table
• New ideas of features / interactions
Should not have
• skeumorphism
• a total rupture from the current design : current users of the app should enjoy the new design and recognize the app without being lost (or not if you have arguments)

```html
<!DOCTYPE html>
<html lang="en">
<head>
<meta charset="utf-8">
<title>Loan Calculator – orOS screens</title>
<link href="https://fonts.googleapis.com/css2?family=Lato:ital,wght@0,300;0,400;0,700;1,400&display=swap" rel="stylesheet">
<style>
:root{
  --bg:#3a3a3a;
  --blue:#52c6f8;
  --blue-mid:#46b1e4;
  --blue-deep:#3a90bd;
  --slice-dark:#2d7498;
  --slice-grey:#b7c6cd;
  --ink:#3c3c3c;
  --muted:#9a9a9a;
  --faint:#b4b4b4;
  --panel:#f4f4f4;
  --line:#dcdcdc;
  --band:#5d5d5d;
  --white:#ffffff;
}
*{box-sizing:border-box;margin:0;padding:0}
html,body{width:1200px;height:1200px;overflow:hidden;background:var(--bg);font-family:'Lato',sans-serif;color:var(--ink)}
.board{position:absolute;left:0;top:0;width:1500px;height:1500px;transform:scale(.8);transform-origin:0 0}
.board-title{position:absolute;left:0;width:1500px;top:40px;text-align:center;font-weight:300;font-size:92px;color:var(--white);letter-spacing:1px}
.board-title span{display:inline-block;border-bottom:4px solid var(--white);line-height:1;padding-bottom:2px}
.screen{position:absolute;width:345px;height:613px;background:var(--white);overflow:hidden;border-top:4px solid var(--blue)}
.t{position:absolute;line-height:1;white-space:nowrap}
.hamburger{position:absolute;left:14px;top:22px;width:20px;height:14px;border-top:2px solid #555;border-bottom:2px solid #555}
.hamburger::after{content:"";position:absolute;left:0;right:0;top:4px;border-top:2px solid #555}
.hdr-title{position:absolute;left:55px;top:22px;font-size:15px;color:#4a4a4a;letter-spacing:.3px}
.hdr-reset{position:absolute;right:14px;top:24px;font-size:12px;color:#666}
.back{position:absolute;left:18px;top:23px;width:10px;height:10px;border-left:1.6px solid #555;border-bottom:1.6px solid #555;transform:rotate(45deg)}
.label{font-size:13.5px;color:#333}
.sub{font-size:8px;color:#777}
.val{font-size:14px;color:#222}
.unit{font-size:9px;color:#333}
.uline{position:absolute;left:232px;width:100px;border-top:1px solid #bdbdbd}
.slider{position:absolute;left:14px;width:318px;height:2px;background:#e2e2e2}
.slider .fill{position:absolute;left:0;top:0;height:2px;background:var(--blue)}
.slider .knob{position:absolute;top:-9px;width:20px;height:20px;margin-left:-10px;border-radius:50%;background:var(--white);border:1.5px solid #e5e5e5}
.slider .knob::after{content:"";position:absolute;left:7px;top:5px;width:3px;height:7px;border-left:1px solid #ccc;border-right:1px solid #ccc}
.panel{position:absolute;left:0;width:345px;background:var(--panel)}
.result-title{font-size:13.5px;color:#333}
.result-sub{font-size:12px;color:var(--muted)}
.big{font-size:21px;color:#222}
.big small{font-size:12px;margin-left:6px}
.chev{position:absolute;width:9px;height:9px;border-right:1.6px solid #333;border-top:1.6px solid #333;transform:rotate(45deg)}
.chev.down{transform:rotate(135deg)}
.cta{position:absolute;left:0;bottom:0;width:345px;height:53px;background:var(--blue);color:var(--white);font-size:15px;text-align:center;line-height:53px;font-weight:400}
.stat{font-size:15px;color:#222}
.stat-sub{font-size:9px;color:#444}
.list-row{position:absolute;left:0;width:345px;height:38px}
.list-row .t{font-size:14px;color:#333}
/* menu screen */
.menu-screen{background:linear-gradient(180deg,#3cbff6 0%,#33a4d6 50%,#2c7ba5 100%)}
.status{font-size:10px;color:var(--white)}
.menu-item{font-size:14.5px;color:#cbeefd}
.menu-item.active{color:var(--white);font-weight:700}
.menu-icon{position:absolute;width:22px;height:18px;border:1.5px solid #cbeefd;border-radius:3px}
.peek{position:absolute;left:250px;top:59px;width:120px;height:490px;background:var(--white);overflow:hidden;box-shadow:-2px 0 6px rgba(0,0,0,.15)}
/* saved loans */
.loan-card{position:absolute;left:0;width:345px;height:76px}
.loan-card.shade{background:var(--panel)}
.cat{font-size:13px;color:#222;letter-spacing:.3px}
.kind{font-size:13px;color:#444}
.bank{font-size:12px;color:#555;font-style:italic}
.meta{font-size:10px;color:#333}
.totals{position:absolute;left:0;bottom:0;width:345px;height:67px;display:flex}
.totals div{flex:1;color:var(--white);text-align:center;padding-top:16px}
.totals b{display:block;font-weight:400;font-size:19px}
.totals span{font-size:10.5px}
.totals div:nth-child(1){background:var(--blue-deep)}
.totals div:nth-child(2){background:var(--blue-mid)}
.totals div:nth-child(3){background:var(--blue)}
.summary-band{position:absolute;left:0;width:345px;height:49px;background:var(--band);color:var(--white)}
/* amortization */
.legend{font-size:11.5px;color:#555}
.dot{position:absolute;width:8px;height:8px;border-radius:50%}
.axis{font-size:7px;color:#444}
.info{font-size:8px;color:#444}
.info em{font-style:normal;font-size:10.5px;color:var(--blue-deep)}
.thead{position:absolute;left:0;top:358px;width:345px;height:30px;background:var(--panel)}
.thead .t{font-size:13px;color:#333;top:9px}
.row .t{font-size:10px;color:var(--faint)}
.row .yr{color:#444}
.row-line{position:absolute;left:0;width:345px;border-top:1px solid #ececec}
</style>
</head>
<body>
<div class="board">

  <h1 class="board-title"><span>Loan Calculator</span></h1>

  <!-- Screen 1 : loan calculator inputs -->
  <section class="screen" style="left:32px;top:205px">
    <div class="hamburger"></div><div class="hdr-title">LOAN CALCULATOR</div><div class="hdr-reset">Reset</div>

    <div class="t label" style="left:15px;top:72px">Amount</div>
    <div class="t val" style="left:239px;top:64px">20,0000</div><div class="t unit" style="left:302px;top:68px">Euro</div>
    <div class="uline" style="top:82px"></div>
    <div class="slider" style="top:98px"><div class="fill" style="width:100px"></div><div class="knob" style="left:100px"></div></div>

    <div class="t label" style="left:15px;top:131px">Payback Period</div>
    <div class="t val" style="left:239px;top:124px">20</div><div class="t unit" style="left:299px;top:128px">Years</div>
    <div class="uline" style="top:142px"></div>
    <div class="slider" style="top:158px"><div class="fill" style="width:170px"></div><div class="knob" style="left:170px"></div></div>

    <div class="t label" style="left:15px;top:181px">Intrest</div>
    <div class="t sub" style="left:15px;top:198px">Nominal annual rate</div>
    <div class="t val" style="left:239px;top:186px">2.5</div><div class="t unit" style="left:314px;top:189px">%</div>
    <div class="uline" style="top:204px"></div>
    <div class="slider" style="top:219px"><div class="fill" style="width:100px"></div><div class="knob" style="left:100px"></div></div>

    <div class="t label" style="left:15px;top:239px">Insurance Fees</div>
    <div class="t sub" style="left:15px;top:256px">Annual rate (% of loan amount)</div>
    <div class="t val" style="left:239px;top:244px">0.3</div><div class="t unit" style="left:299px;top:248px">Years</div>
    <div class="uline" style="top:262px"></div>
    <div class="slider" style="top:280px"><div class="fill" style="width:170px"></div><div class="knob" style="left:170px"></div></div>

    <div class="t label" style="left:15px;top:298px">One-time fees</div>
    <div class="t sub" style="left:15px;top:315px">Origination fees, Closing Cost...</div>
    <div class="t val" style="left:239px;top:303px">1000</div><div class="t unit" style="left:302px;top:307px">Euro</div>
    <div class="uline" style="top:321px"></div>
    <div class="slider" style="top:340px"><div class="fill" style="width:170px"></div><div class="knob" style="left:170px"></div></div>

    <div class="panel" style="top:362px;height:251px"></div>
    <div class="t result-title" style="left:15px;top:381px">Result</div>
    <div class="t result-sub" style="left:16px;top:404px">Loan payment require per Month</div>
    <div class="t big" style="left:213px;top:398px">1109.81<small>Euro</small></div>

    <svg style="position:absolute;left:0;top:416px" width="345" height="197" viewBox="0 0 345 197">
      <g transform="translate(168 117)">
        <path d="M0 0 L72.7 6.4 A73 73 0 1 1 -25 -68.6 Z" fill="#52c6f8"/>
        <path d="M0 0 L-25 -68.6 A73 73 0 0 1 68.6 -25 Z" fill="#2d7498"/>
        <path d="M0 0 L68.6 -25 A73 73 0 0 1 72.7 6.4 Z" fill="#b7c6cd"/>
      </g>
      <g stroke="#111" stroke-width="1.3" fill="none">
        <polyline points="93,39 123,39 123,117"/>
        <polyline points="212,29 183,29 183,85"/>
        <polyline points="226,101 264,101"/>
      </g>
      <g fill="#111"><circle cx="93" cy="39" r="2"/><circle cx="123" cy="117" r="2"/><circle cx="212" cy="29" r="2"/><circle cx="183" cy="85" r="2"/><circle cx="226" cy="101" r="2"/><circle cx="264" cy="101" r="2"/></g>
      <g font-family="Lato, sans-serif" font-size="10.5" fill="#111">
        <text x="48" y="33">Capital</text><text x="62" y="47">70%</text>
        <text x="219" y="33">Intrest</text><text x="233" y="47">25%</text>
        <text x="285" y="99">Insur</text><text x="294" y="113">4%</text>
      </g>
    </svg>
  </section>

  <!-- Screen 2 : loan calculator result -->
  <section class="screen" style="left:397px;top:205px">
    <div class="hamburger"></div><div class="hdr-title">LOAN CALCULATOR</div><div class="hdr-reset">Reset</div>
    <div class="panel" style="top:58px;height:340px"></div>
    <div class="t result-title" style="left:15px;top:81px">Result</div>
    <div class="t result-sub" style="left:16px;top:104px">Loan payment require per Month</div>
    <div class="t big" style="left:213px;top:98px">1109.81<small>Euro</small></div>

    <svg style="position:absolute;left:0;top:120px" width="345" height="220" viewBox="0 0 345 220">
      <g transform="translate(168 113)">
        <path d="M0 0 L72.7 6.4 A73 73 0 1 1 -25 -68.6 Z" fill="#52c6f8"/>
        <path d="M0 0 L-25 -68.6 A73 73 0 0 1 68.6 -25 Z" fill="#2d7498"/>
        <path d="M0 0 L68.6 -25 A73 73 0 0 1 72.7 6.4 Z" fill="#b7c6cd"/>
      </g>
      <g stroke="#111" stroke-width="1.3" fill="none">
        <polyline points="93,33 124,33 124,113"/>
        <polyline points="213,25 183,25 183,80"/>
        <polyline points="226,98 265,98"/>
      </g>
      <g fill="#111"><circle cx="93" cy="33" r="2"/><circle cx="124" cy="113" r="2"/><circle cx="213" cy="25" r="2"/><circle cx="183" cy="80" r="2"/><circle cx="226" cy="98" r="2"/><circle cx="265" cy="98" r="2"/></g>
      <g font-family="Lato, sans-serif" font-size="10.5" fill="#111">
        <text x="48" y="27">Capital</text><text x="62" y="41">70%</text>
        <text x="220" y="29">Intrest</text><text x="234" y="43">25%</text>
        <text x="285" y="92">Insur</text><text x="294" y="106">4%</text>
      </g>
    </svg>

    <svg style="position:absolute;left:0;top:335px" width="345" height="60" viewBox="0 0 345 60">
      <g stroke="#555" stroke-width="1" fill="none">
        <line x1="10" y1="1" x2="335" y2="1"/>
        <line x1="15" y1="12" x2="15" y2="55"/><line x1="120" y1="12" x2="120" y2="55"/>
        <line x1="222" y1="12" x2="222" y2="55"/><line x1="326" y1="12" x2="326" y2="55"/>
        <line x1="15" y1="55" x2="326" y2="55"/>
      </g>
    </svg>
    <div class="t stat" style="left:25px;top:358px">€67353.39</div><div class="t stat-sub" style="left:26px;top:376px">Total cost of credit</div>
    <div class="t stat" style="left:131px;top:358px">€267353.38</div><div class="t stat-sub" style="left:132px;top:376px">Total of payment</div>
    <div class="t stat" style="left:233px;top:358px">3.06%</div><div class="t stat-sub" style="left:234px;top:376px">Nominal APR</div>

    <div class="t" style="left:17px;top:433px;font-size:14px;color:#333">Amortization Table</div>
    <div class="t sub" style="left:17px;top:452px;color:#999">select a monthly payment to compute refinancing</div>
    <div class="chev" style="left:315px;top:441px"></div>

    <div class="list-row" style="top:470px;background:var(--panel)"><div class="t" style="left:17px;top:12px">Start Month</div><div class="t" style="left:171px;top:12px">Not Set</div><div class="chev" style="left:315px;top:14px"></div></div>
    <div class="list-row" style="top:508px"><div class="t" style="left:17px;top:12px">Detailed Notary Fees</div><div class="chev" style="left:315px;top:14px"></div></div>
    <div class="list-row" style="top:546px;background:var(--panel)"><div class="t" style="left:17px;top:12px">Advance Setting</div><div class="chev" style="left:315px;top:14px"></div></div>
  </section>

  <!-- Screen 3 : side menu -->
  <section class="screen menu-screen" style="left:758px;top:205px;border-top:none">
    <div class="t status" style="left:6px;top:3px">●●●○○ NIMBUS</div>
    <div class="t status" style="left:151px;top:3px">4:21 PM</div>
    <div class="t status" style="left:290px;top:3px">22%</div>
    <div style="position:absolute;left:316px;top:4px;width:20px;height:8px;border:1px solid #fff;border-radius:2px"><div style="width:4px;height:100%;background:#fff"></div></div>

    <div role="img" aria-label="Profile photo of the signed-in user" style="position:absolute;left:31px;top:89px;width:66px;height:66px;border-radius:50%;border:2px solid #fff;background:linear-gradient(160deg,#c9d6dd,#8fa3ad)"></div>
    <div class="t" style="left:111px;top:105px;font-size:15px;color:#fff">Alex Marlowe</div>
    <div class="t" style="left:111px;top:124px;font-size:12px;color:#bfe9fb">Westbay, USA</div>

    <div class="menu-icon" style="left:42px;top:224px;border-radius:50%;width:20px"></div>
    <div class="t menu-item" style="left:86px;top:226px">Capacity</div>
    <div class="menu-icon" style="left:40px;top:279px;border-color:#fff"></div>
    <div style="position:absolute;left:58px;top:288px;width:13px;height:13px;border-radius:50%;background:#fff"></div>
    <div class="t menu-item active" style="left:86px;top:282px">Loan Calculator</div>
    <div class="menu-icon" style="left:42px;top:333px;border-radius:50%;width:20px"></div>
    <div class="t menu-item" style="left:86px;top:336px">Saved Loans</div>
    <div class="t menu-item" style="left:41px;top:389px;font-size:11px;color:#fff">●●○</div>
    <div class="t menu-item" style="left:86px;top:390px">More</div>

    <div class="peek">
      <div class="hamburger" style="left:12px;top:18px;width:16px;height:11px;border-width:1.5px"></div>
      <div class="t" style="left:44px;top:18px;font-size:12px;color:#555">LOAN CALCULATOR</div>
      <div style="position:absolute;left:0;top:50px;width:120px;height:255px;background:var(--panel)"></div>
      <svg style="position:absolute;left:0;top:50px" width="120" height="260" viewBox="0 0 120 260">
        <circle cx="112" cy="120" r="60" fill="#52c6f8"/>
        <polyline points="48,38 82,38 82,120" fill="none" stroke="#111" stroke-width="1.2"/>
        <circle cx="82" cy="120" r="2" fill="#111"/>
        <g font-family="Lato, sans-serif" font-size="8" fill="#111"><text x="35" y="22">Capital</text><text x="46" y="31">70%</text></g>
        <line x1="8" y1="228" x2="120" y2="228" stroke="#555"/>
        <line x1="12" y1="234" x2="12" y2="262" stroke="#555"/>
      </svg>
      <div class="t" style="left:20px;top:285px;font-size:12px;color:#222">€67353.39</div>
      <div class="t" style="left:21px;top:299px;font-size:6.5px;color:#444">Total cost of credit</div>
      <div class="t" style="left:14px;top:346px;font-size:11.5px;color:#333">Amortization Table</div>
      <div class="t" style="left:14px;top:361px;font-size:6.5px;color:#999">select a monthly payment to compute</div>
      <div style="position:absolute;left:0;top:374px;width:120px;height:30px;background:var(--panel)"></div>
      <div class="t" style="left:14px;top:383px;font-size:11.5px;color:#333">Start Month</div>
      <div class="t" style="left:14px;top:413px;font-size:11.5px;color:#333">Detailed Notary Fees</div>
      <div style="position:absolute;left:0;top:434px;width:120px;height:30px;background:var(--panel)"></div>
      <div class="t" style="left:14px;top:443px;font-size:11.5px;color:#333">Advance Setting</div>
    </div>
  </section>

  <!-- Screen 4 : credit capacity -->
  <section class="screen" style="left:1123px;top:205px">
    <div class="hamburger"></div><div class="hdr-title">CREDIT CAPACITY</div><div class="hdr-reset">Reset</div>

    <div class="t label" style="left:15px;top:83px">Total Monthly Income</div>
    <div class="t val" style="left:239px;top:82px">5,000</div><div class="t unit" style="left:302px;top:86px">Euro</div>
    <div class="uline" style="top:100px"></div>
    <div class="slider" style="top:127px"><div class="fill" style="width:100px"></div><div class="knob" style="left:100px"></div></div>

    <div class="t label" style="left:15px;top:168px">Monthly Loan Payments</div>
    <div class="t val" style="left:239px;top:167px">1,200</div><div class="t unit" style="left:302px;top:171px">Euro</div>
    <div class="uline" style="top:185px"></div>
    <div class="slider" style="top:212px"><div class="fill" style="width:192px"></div><div class="knob" style="left:192px"></div></div>

    <div class="t label" style="left:15px;top:252px">Debt-To-Income Max Ratio</div>
    <div class="t val" style="left:239px;top:251px">33</div><div class="t unit" style="left:314px;top:255px">%</div>
    <div class="uline" style="top:269px"></div>
    <div class="slider" style="top:296px"><div class="fill" style="width:100px"></div><div class="knob" style="left:100px"></div></div>

    <div class="panel" style="top:336px;height:225px"></div>
    <div class="t" style="left:33px;top:368px;font-size:15px;color:#a6a6a6">Credit Capacity</div>
    <div class="t big" style="left:232px;top:365px">1650<small style="font-size:16px;margin-left:2px">Euro</small></div>
    <div style="position:absolute;left:20px;top:403px;width:320px;border-top:1px solid #e6e6e6"></div>
    <div class="t" style="left:58px;top:430px;font-size:15px;color:#a6a6a6">Current DTI</div>
    <div class="t big" style="left:246px;top:426px;font-size:23px">24.00<small style="font-size:14px;margin-left:2px">%</small></div>
    <div style="position:absolute;left:20px;top:468px;width:320px;border-top:1px solid #e6e6e6"></div>
    <div class="t" style="left:20px;top:488px;font-size:15px;color:#a6a6a6;text-align:center;width:120px;white-space:normal;line-height:.95">Amount Available for new Loan</div>
    <div class="t big" style="left:246px;top:491px;font-size:23px">24.00<small style="font-size:14px;margin-left:2px">%</small></div>
    <div class="cta">HOW MUCH I BORROW?</div>
  </section>

  <!-- Screen 5 : how much -->
  <section class="screen" style="left:32px;top:842px">
    <div class="back"></div><div class="hdr-title" style="left:48px">HOW MUCH?</div><div class="hdr-reset">Reset</div>

    <div class="t label" style="left:15px;top:83px">Monthly Payment</div>
    <div class="t val" style="left:239px;top:82px">450</div><div class="t unit" style="left:302px;top:86px">Euro</div>
    <div class="uline" style="top:100px"></div>
    <div class="slider" style="top:127px"><div class="fill" style="width:100px"></div><div class="knob" style="left:100px"></div></div>

    <div class="t label" style="left:15px;top:168px">Period</div>
    <div class="t val" style="left:239px;top:167px">120</div><div class="t unit" style="left:289px;top:171px">Months</div>
    <div class="uline" style="top:185px"></div>
    <div class="slider" style="top:212px"><div class="fill" style="width:192px"></div><div class="knob" style="left:192px"></div></div>

    <div class="t label" style="left:15px;top:252px">Annual Intrest Rate</div>
    <div class="t val" style="left:239px;top:251px">5</div><div class="t unit" style="left:314px;top:255px">%</div>
    <div class="uline" style="top:269px"></div>
    <div class="slider" style="top:296px"><div class="fill" style="width:100px"></div><div class="knob" style="left:100px"></div></div>

    <div class="t label" style="left:15px;top:344px">Annual Intrest Rate</div>
    <div style="position:absolute;left:278px;top:337px;width:54px;height:24px;border-radius:12px;background:#d6d6d6"><div style="position:absolute;left:1px;top:1px;width:22px;height:22px;border-radius:50%;background:#fff"></div></div>

    <div class="panel" style="top:450px;height:163px"></div>
    <div class="t" style="left:22px;top:498px;font-size:15px;color:#a6a6a6">Amount</div>
    <div class="t big" style="left:169px;top:493px;font-size:23px">42, 427,04<small style="font-size:15px;margin-left:9px">Euro</small></div>
    <div class="cta">LOAD VALUE IN CALCULATOR</div>
  </section>

  <!-- Screen 6 : saved loans -->
  <section class="screen" style="left:397px;top:842px">
    <div class="hamburger"></div><div class="hdr-title">SAVED LOANS</div>

    <div class="loan-card shade" style="top:58px">
      <div class="t cat" style="left:15px;top:15px">HOUSING</div>
      <div class="t kind" style="left:28px;top:34px">Home</div><div class="t bank" style="left:251px;top:34px">Banco</div>
      <div class="t meta" style="left:28px;top:54px">€200 000.00</div><div class="t meta" style="left:106px;top:54px">20 years</div>
      <div class="t meta" style="left:179px;top:54px">2.50%</div><div class="t meta" style="left:237px;top:54px">Ins. 0.30%</div>
      <div class="chev" style="left:316px;top:40px;width:11px;height:11px;border-width:2px"></div>
    </div>
    <div class="loan-card" style="top:136px">
      <div class="t cat" style="left:15px;top:15px">VEHICLE</div>
      <div class="t kind" style="left:28px;top:34px">Car</div><div class="t bank" style="left:268px;top:34px">mtl</div>
      <div class="t meta" style="left:28px;top:54px">€550 000.00</div><div class="t meta" style="left:101px;top:54px">84 months</div>
      <div class="t meta" style="left:179px;top:54px">3.61%</div>
      <div class="chev" style="left:316px;top:40px;width:11px;height:11px;border-width:2px"></div>
    </div>
    <div class="loan-card shade" style="top:214px">
      <div class="t cat" style="left:15px;top:15px">HOUSING</div>
      <div class="t kind" style="left:28px;top:34px">Flat</div><div class="t bank" style="left:251px;top:34px">Banco</div>
      <div class="t meta" style="left:28px;top:54px">€100 000.00</div><div class="t meta" style="left:106px;top:54px">10 years</div>
      <div class="t meta" style="left:179px;top:54px">2.50%</div><div class="t meta" style="left:237px;top:54px">Ins. 0.30%</div>
      <div class="chev" style="left:316px;top:40px;width:11px;height:11px;border-width:2px"></div>
    </div>

    <div class="totals">
      <div><b>€ 1851.76</b><span>Monthly Payments</span></div>
      <div><b>€ 25500000</b><span>Monthly Payments</span></div>
      <div><b>€ 74677</b><span>Monthly Payments</span></div>
    </div>
  </section>

  <!-- Screen 7 : saved loans expanded -->
  <section class="screen" style="left:758px;top:842px">
    <div class="hamburger"></div><div class="hdr-title">SAVED LOANS</div>

    <div class="loan-card shade" style="top:58px">
      <div class="t cat" style="left:15px;top:15px">HOUSING</div>
      <div class="t kind" style="left:28px;top:34px">Home</div><div class="t bank" style="left:251px;top:34px">Banco</div>
      <div class="t meta" style="left:28px;top:54px">€200 000.00</div><div class="t meta" style="left:106px;top:54px">20 years</div>
      <div class="t meta" style="left:179px;top:54px">2.50%</div><div class="t meta" style="left:237px;top:54px">Ins. 0.30%</div>
      <div class="chev down" style="left:318px;top:36px;width:11px;height:11px;border-width:2px"></div>
    </div>
    <div class="summary-band" style="top:134px">
      <div class="t" style="left:15px;top:10px;font-size:19px">€ 1109.81</div><div class="t" style="left:43px;top:32px;font-size:8.5px">/month</div>
      <div class="t" style="left:125px;top:10px;font-size:19px">€ 67353.39</div><div class="t" style="left:166px;top:32px;font-size:8.5px">cost</div>
      <div class="t" style="left:261px;top:10px;font-size:19px">3.06%</div><div class="t" style="left:266px;top:32px;font-size:8.5px">Nom. APR</div>
    </div>
    <div class="loan-card" style="top:184px">
      <div class="t cat" style="left:15px;top:14px">VEHICLE</div>
      <div class="t kind" style="left:28px;top:33px">Car</div><div class="t bank" style="left:268px;top:33px">mtl</div>
      <div class="t meta" style="left:28px;top:53px">€550 000.00</div><div class="t meta" style="left:101px;top:53px">84 months</div>
      <div class="t meta" style="left:179px;top:53px">3.61%</div>
      <div class="chev" style="left:316px;top:40px;width:11px;height:11px;border-width:2px"></div>
    </div>
    <div class="loan-card shade" style="top:262px">
      <div class="t cat" style="left:15px;top:14px">HOUSING</div>
      <div class="t kind" style="left:28px;top:33px">Flat</div><div class="t bank" style="left:251px;top:33px">Banco</div>
      <div class="t meta" style="left:28px;top:53px">€100 000.00</div><div class="t meta" style="left:106px;top:53px">10 years</div>
      <div class="t meta" style="left:179px;top:53px">2.50%</div><div class="t meta" style="left:237px;top:53px">Ins. 0.30%</div>
      <div class="chev" style="left:316px;top:40px;width:11px;height:11px;border-width:2px"></div>
    </div>

    <div class="totals">
      <div><b>€ 1851.76</b><span>Monthly Payments</span></div>
      <div><b>€ 25500000</b><span>Monthly Payments</span></div>
      <div><b>€ 74677</b><span>Monthly Payments</span></div>
    </div>
  </section>

  <!-- Screen 8 : amortization -->
  <section class="screen" style="left:1123px;top:842px">
    <div class="back"></div><div class="hdr-title" style="left:39px">AMORTIZATION</div>
    <svg style="position:absolute;left:310px;top:18px" width="20" height="20" viewBox="0 0 20 20" fill="none" stroke="#555" stroke-width="1.5">
      <path d="M9 2H2v16h16v-7"/><path d="M12 2h6v6M18 2l-8 8"/>
    </svg>

    <div class="dot" style="left:78px;top:64px;background:var(--blue)"></div><div class="t legend" style="left:93px;top:62px">Insurance</div>
    <div class="dot" style="left:170px;top:64px;background:var(--slice-dark)"></div><div class="t legend" style="left:185px;top:62px">Interest</div>
    <div class="dot" style="left:258px;top:64px;background:var(--slice-grey)"></div><div class="t legend" style="left:274px;top:62px">Principal</div>

    <div class="t axis" style="left:2px;top:80px">100%</div>
    <div class="t axis" style="left:2px;top:163px">56.8%</div>
    <div class="t axis" style="left:10px;top:259px">0%</div>
    <svg style="position:absolute;left:0;top:80px" width="345" height="190" viewBox="0 0 345 190">
      <rect x="27" y="5" width="300" height="180" fill="#52c6f8"/>
      <path d="M27 12 H327 V27 L27 91 Z" fill="#2d7498"/>
      <rect x="27" y="5" width="300" height="7" fill="#b7c6cd"/>
      <line x1="27" y1="5" x2="27" y2="185" stroke="#444"/>
      <line x1="27" y1="185" x2="327" y2="185" stroke="#444"/>
    </svg>

    <div class="t" style="left:119px;top:280px;font-size:10.5px;color:#333">Amount</div>
    <div class="t" style="left:151px;top:276px;font-size:16px;color:var(--blue-deep)">€200000.00</div>

    <div class="t info" style="left:15px;top:308px">Period <em>20 years</em></div>
    <div class="t info" style="left:145px;top:308px">Rate <em>2.50 %</em></div>
    <div class="t info" style="left:273px;top:308px">Insur. <em>0.30%</em></div>
    <div class="t info" style="left:7px;top:330px">Payment <em>€1109.81</em></div>
    <div class="t info" style="left:145px;top:330px">Cost <em>€67353.39</em></div>
    <div class="t info" style="left:258px;top:330px">Nom APR <em>3.06%</em></div>

    <div class="thead">
      <div class="t" style="left:10px">Year</div><div class="t" style="left:60px">Principal</div>
      <div class="t" style="left:135px">Intrest</div><div class="t" style="left:199px">Insur.</div>
      <div class="t" style="left:271px">Balance</div>
    </div>

    <div class="row" style="position:absolute;left:0;top:388px;width:345px;height:240px">
      <div class="t yr" style="left:16px;top:11px;font-size:10px">01</div><div class="t" style="left:61px;top:11px">€7806.78</div><div class="t" style="left:131px;top:11px">€4910.96</div><div class="t" style="left:191px;top:11px">€600..00</div><div class="t" style="left:252px;top:11px">€192 193.24</div><div class="chev" style="left:326px;top:12px;width:7px;height:7px;border-width:1.3px"></div>
      <div class="row-line" style="top:29px"></div>
      <div class="t yr" style="left:16px;top:41px;font-size:10px">02</div><div class="t" style="left:61px;top:41px">€7806.78</div><div class="t" style="left:131px;top:41px">€4910.96</div><div class="t" style="left:191px;top:41px">€600..00</div><div class="t" style="left:252px;top:41px">€192 193.24</div><div class="chev" style="left:326px;top:42px;width:7px;height:7px;border-width:1.3px"></div>
      <div class="row-line" style="top:59px"></div>
      <div class="t yr" style="left:16px;top:70px;font-size:10px">03</div><div class="t" style="left:61px;top:70px">€7806.78</div><div class="t" style="left:131px;top:70px">€4910.96</div><div class="t" style="left:191px;top:70px">€600..00</div><div class="t" style="left:252px;top:70px">€192 193.24</div><div class="chev" style="left:326px;top:71px;width:7px;height:7px;border-width:1.3px"></div>
      <div class="row-line" style="top:88px"></div>
      <div class="t yr" style="left:16px;top:100px;font-size:10px">04</div><div class="t" style="left:61px;top:100px">€7806.78</div><div class="t" style="left:131px;top:100px">€4910.96</div><div class="t" style="left:191px;top:100px">€600..00</div><div class="t" style="left:252px;top:100px">€192 193.24</div><div class="chev" style="left:326px;top:101px;width:7px;height:7px;border-width:1.3px"></div>
      <div class="row-line" style="top:118px"></div>
      <div class="t yr" style="left:16px;top:129px;font-size:10px">05</div><div class="t" style="left:61px;top:129px">€7806.78</div><div class="t" style="left:131px;top:129px">€4910.96</div><div class="t" style="left:191px;top:129px">€600..00</div><div class="t" style="left:252px;top:129px">€192 193.24</div><div class="chev" style="left:326px;top:130px;width:7px;height:7px;border-width:1.3px"></div>
      <div class="row-line" style="top:147px"></div>
      <div class="t yr" style="left:16px;top:159px;font-size:10px">06</div><div class="t" style="left:61px;top:159px">€7806.78</div><div class="t" style="left:131px;top:159px">€4910.96</div><div class="t" style="left:191px;top:159px">€600..00</div><div class="t" style="left:252px;top:159px">€192 193.24</div><div class="chev" style="left:326px;top:160px;width:7px;height:7px;border-width:1.3px"></div>
      <div class="row-line" style="top:177px"></div>
      <div class="t yr" style="left:16px;top:189px;font-size:10px">07</div><div class="t" style="left:61px;top:189px">€7806.78</div><div class="t" style="left:131px;top:189px">€4910.96</div><div class="t" style="left:191px;top:189px">€600..00</div><div class="t" style="left:252px;top:189px">€192 193.24</div><div class="chev" style="left:326px;top:190px;width:7px;height:7px;border-width:1.3px"></div>
      <div class="row-line" style="top:207px"></div>
      <div class="t yr" style="left:16px;top:219px;font-size:10px">08</div><div class="t" style="left:61px;top:219px">€7806.78</div><div class="t" style="left:131px;top:219px">€4910.96</div><div class="t" style="left:191px;top:219px">€600..00</div><div class="t" style="left:252px;top:219px">€192 193.24</div><div class="chev" style="left:326px;top:220px;width:7px;height:7px;border-width:1.3px"></div>
    </div>
  </section>

</div>
</body>
</html>
```